Tovrelan Ltda

Logo design focused on: - Construction of civil works - Electrical services - Metal structures - Equipment rental Tomás Ibarra Leiva Manager tovrelan.ltda@brevomail.example 56 9 48215037 Quelitoco s / n, Sorimar, San Pedro de Atacama

Building

Colors
33a6d7
0292cd
33b8a4
0555a3

```html
<!DOCTYPE html>
<html lang="es">
<head>
<meta charset="utf-8">
<title>Tovrelan Ltda — Tarjeta de presentación</title>
<link href="https://fonts.googleapis.com/css2?family=Roboto:wght@400;500;700&display=swap" rel="stylesheet">
<style>
  :root {
    --blue-deep: #0555a3;
    --blue-main: #0292cd;
    --blue-sky: #33a6d7;
    --teal: #33b8a4;
    --white: #ffffff;
    --stage: #2b2b2d;
    --card-blue: #0a6fc0;
  }
  * { margin: 0; padding: 0; box-sizing: border-box; }
  html, body {
    width: 1200px; height: 900px; overflow: hidden;
    background: var(--stage);
    font-family: "Roboto", Arial, sans-serif;
  }
  .canvas { position: relative; width: 1200px; height: 900px; }

  .card {
    position: absolute;
    width: 540px; height: 310px;
    border-radius: 22px;
    overflow: hidden;
    box-shadow: 0 18px 40px rgba(0,0,0,0.45);
  }

  /* Front */
  .card-front { left: 40px; top: 340px; background: var(--white); }
  .card-front .waves { position: absolute; inset: 0; }
  .brand {
    position: absolute; display: flex; align-items: center; gap: 10px;
    font-weight: 500; letter-spacing: 2px; text-transform: uppercase;
  }
  .card-front .brand { left: 24px; top: 16px; color: var(--blue-deep); font-size: 21px; }
  .brand-dot { width: 34px; height: 34px; border-radius: 50%; background: var(--teal); flex: none; }

  .services {
    position: absolute; left: 20px; top: 135px;
    list-style: none; color: var(--white); font-size: 12px; line-height: 16px;
  }

  .person { position: absolute; right: 26px; top: 96px; text-align: right; }
  .person-name { color: var(--blue-main); font-size: 23px; font-weight: 500; text-transform: uppercase; line-height: 27px; }
  .person-role { color: var(--teal); font-size: 16px; margin-top: 2px; }
  .edge-tab { position: absolute; right: 0; top: 130px; width: 10px; height: 40px; background: var(--teal); }

  .contact {
    position: absolute; right: 200px; bottom: 14px;
    list-style: none; color: var(--white); font-size: 14px; line-height: 22px; text-align: right;
  }
  .contact li { display: flex; align-items: center; justify-content: flex-end; gap: 8px; }
  .contact svg { width: 13px; height: 13px; flex: none; }

  /* Back */
  .card-back {
    left: 620px; top: 130px;
    background: linear-gradient(160deg, var(--card-blue), var(--blue-main) 60%, var(--blue-deep));
  }
  .card-back .brand {
    left: 0; right: 0; top: 0; bottom: 0; justify-content: center;
    color: var(--white); font-size: 30px;
  }
  .card-back .brand-dot { width: 52px; height: 52px; }
</style>
</head>
<body>
<main class="canvas">

  <section class="card card-front" aria-label="Tarjeta, cara frontal">
    <svg class="waves" viewBox="0 0 540 310" preserveAspectRatio="none" aria-hidden="true">
      <path d="M0,70 C140,66 215,100 270,150 C325,205 415,245 462,310 L0,310 Z" fill="#33b8a4"/>
      <path d="M0,90 C130,86 200,118 252,168 C305,222 395,258 438,310 L0,310 Z" fill="#0a6fc0"/>
    </svg>

    <div class="brand"><span class="brand-dot"></span><span>Tovrelan Ltda</span></div>

    <ul class="services">
      <li>Construcción de Obras Civiles</li>
      <li>Servicios eléctricos</li>
      <li>Estructuras metálicas</li>
      <li>Arriendo de Equipos</li>
    </ul>

    <div class="person">
      <p class="person-name">Tomás Ibarra Leiva</p>
      <p class="person-role">Gerente</p>
    </div>
    <span class="edge-tab"></span>

    <ul class="contact">
      <li>+56 9 48215037
        <svg viewBox="0 0 24 24" aria-hidden="true"><path fill="#fff" d="M6.6 10.8a15 15 0 0 0 6.6 6.6l2.2-2.2c.3-.3.7-.4 1-.2 1.1.4 2.3.6 3.6.6.6 0 1 .4 1 1V20c0 .6-.4 1-1 1A17 17 0 0 1 3 4c0-.6.4-1 1-1h3.5c.6 0 1 .4 1 1 0 1.3.2 2.5.6 3.6.1.3 0 .7-.2 1z"/></svg>
      </li>
      <li>tovrelan.ltda@brevomail.example
        <svg viewBox="0 0 24 24" aria-hidden="true"><rect x="3" y="5" width="18" height="14" rx="1.5" fill="none" stroke="#fff" stroke-width="2"/><path d="M3 6l9 7 9-7" fill="none" stroke="#fff" stroke-width="2"/></svg>
      </li>
    </ul>
  </section>

  <section class="card card-back" aria-label="Tarjeta, cara posterior">
    <div class="brand"><span class="brand-dot"></span><span>Tovrelan Ltda</span></div>
  </section>

</main>
</body>
</html>
```